Elmrow Management real estate management company needs presentation folder to hand clients

looking for a folder with pockets that represent my real estate management company when i hand to client reports or promotional material. I only do resedential real estate. I want classy and professional - pictures or additioal graphixs are fine

when a client open i will usally insert text and reports about my business
also on the inside flap is usally place for my business card i will upload a picture so the theme can be constant

Target Market(s)

my existing real estate cleints
and i will use when i am soliciting new business

Industry/Entity Type

Real Estate

Font styles to use
Serif

Requirements
Must have
• must have logo
• must give appearance of professionalism and maturity
• have basic company info tel# ,address
• id like viewer to know I manage real estate - focus on residential small to large apartment buildings
• not strip malls, not giganic complexes - im a mid size company
• logo is black but i welcome color as u see fit
Nice to have
• maybe pictures
• my slogan - " we will manage your building like its our own "
• focus on professioanl, safe, trust worthy
• type style should be clear and readable - but im open to sugestions

```html
<!DOCTYPE html>
<html lang="en">
<head>
<meta charset="utf-8">
<title>Elmrow Management – Presentation Folder</title>
<link rel="stylesheet" href="https://fonts.googleapis.com/css2?family=Cormorant+Garamond:wght@600&family=Marcellus&display=swap">
<style>
  :root {
    --paper: #e6e6e9;
    --paper-light: #f3f3f5;
    --paper-shade: #c9c9cf;
    --ink: #121214;
    --frame: #2a2a33;
    --band: #d7d7dc;
    --brand: #2e3122;
    --white: #ffffff;
  }
  html, body {
    margin: 0;
    padding: 0;
    width: 927px;
    height: 1200px;
    overflow: hidden;
    background: var(--paper);
  }
  .folder {
    position: relative;
    width: 927px;
    height: 1200px;
    overflow: hidden;
    background: linear-gradient(135deg, var(--paper-light), var(--paper) 55%, var(--paper-shade));
  }
  .folder-art {
    position: absolute;
    inset: 0;
    width: 927px;
    height: 1200px;
  }
  .brand {
    position: absolute;
    left: 58px;
    top: 98px;
    width: 290px;
    display: flex;
    align-items: center;
    gap: 12px;
    font-family: "Cormorant Garamond", serif;
    font-weight: 600;
    font-size: 30px;
    line-height: 1.05;
    letter-spacing: 2px;
    color: var(--brand);
    text-transform: uppercase;
  }
  .brand-mark {
    flex: none;
    width: 18px;
    height: 18px;
    background: var(--brand);
  }
  .slogan {
    font-family: "Marcellus", serif;
    font-size: 21px;
    letter-spacing: 1px;
    fill: var(--white);
  }
  .service-line {
    position: absolute;
    left: 312px;
    top: 1062px;
    width: 600px;
    height: 46px;
    background: linear-gradient(90deg, rgba(255,255,255,0.55), var(--white) 20%, var(--white) 85%, rgba(255,255,255,0.6));
    display: flex;
    align-items: center;
    justify-content: center;
    font-family: "Cormorant Garamond", serif;
    font-weight: 600;
    font-size: 31px;
    letter-spacing: 0.5px;
    color: var(--ink);
  }
</style>
</head>
<body>
<main class="folder">
  <svg class="folder-art" viewBox="0 0 1159 1500" xmlns="http://www.w3.org/2000/svg">
    <defs>
      <linearGradient id="column" x1="0" y1="0" x2="1" y2="0">
        <stop offset="0" stop-color="#d4d4d9"/>
        <stop offset="0.5" stop-color="#e4e4e8"/>
        <stop offset="1" stop-color="#cfcfd5"/>
      </linearGradient>
      <linearGradient id="slogan-band" x1="0" y1="1" x2="1" y2="0">
        <stop offset="0" stop-color="#b9b9c0"/>
        <stop offset="0.5" stop-color="#dcdce1"/>
        <stop offset="1" stop-color="#9d9da6"/>
      </linearGradient>
      <linearGradient id="aerial" x1="0" y1="0" x2="1" y2="1">
        <stop offset="0" stop-color="#8e8a9e"/>
        <stop offset="0.3" stop-color="#6f7340"/>
        <stop offset="0.55" stop-color="#b6b3b8"/>
        <stop offset="0.8" stop-color="#6b6f52"/>
        <stop offset="1" stop-color="#cfcdd3"/>
      </linearGradient>
      <linearGradient id="lower-band" x1="0" y1="0" x2="0" y2="1">
        <stop offset="0" stop-color="#2b2b35"/>
        <stop offset="1" stop-color="#3b3b47"/>
      </linearGradient>
    </defs>

    <!-- outer bevel frame -->
    <rect class="edge" x="0" y="0" width="1159" height="1500" fill="none" stroke="#d0d0d6" stroke-width="30"/>
    <rect class="edge-inner" x="30" y="30" width="1099" height="1440" fill="none" stroke="#f7f7f9" stroke-width="4"/>

    <!-- left column panel -->
    <rect class="left-column" x="40" y="560" width="305" height="910" fill="url(#column)"/>
    <rect class="column-rule" x="345" y="500" width="36" height="1000" fill="#f6f6f8"/>

    <!-- diagonal slogan band -->
    <polygon class="slogan-band" points="0,560 1159,130 1159,175 381,463 381,500 0,640" fill="url(#slogan-band)"/>
    <polygon class="black-stripe" points="0,548 1159,98 1159,135 0,585" fill="var(--ink)"/>
    <polygon class="white-rule" points="0,540 1159,88 1159,96 0,548" fill="var(--white)"/>

    <!-- photo frame -->
    <polygon class="photo-frame" points="382,430 1159,140 1159,1245 382,1100" fill="var(--frame)"/>
    <polygon class="lower-band" points="382,1080 1159,1080 1159,1250 382,1105" fill="url(#lower-band)"/>
    <polygon class="lower-highlight" points="382,1105 1159,1250 1159,1262 382,1117" fill="#f5f5f7"/>

    <!-- aerial image area -->
    <g role="img" aria-label="Aerial photograph of a residential neighbourhood with mid-size apartment buildings, a traffic circle and tree-lined streets">
      <polygon class="aerial-photo" points="432,455 1110,285 1110,1075 630,1075 432,1040" fill="url(#aerial)" stroke="#f2f2f4" stroke-width="4"/>
    </g>

    <!-- slogan -->
    <text class="slogan" transform="translate(450,425) rotate(-20.6)">WE WILL MANAGE YOUR BUILDING LIKE IT IS OUR OWN</text>
  </svg>

  <div class="brand">
    <span class="brand-mark"></span>
    <span class="brand-name">Elmrow Management</span>
  </div>

  <div class="service-line">REAL ESTATE MANAGEMENT</div>
</main>
</body>
</html>
```